Copper Ridge Inquiries Letterhead

I would like to design a letterhead for a private investigation company. Our primary clients will be law firms. The business card is included below

```html
<!DOCTYPE html>
<html lang="en">
<head>
<meta charset="utf-8">
<title>Copper Ridge Inquiries — Letterhead</title>
<link href="https://fonts.googleapis.com/css2?family=Open+Sans:wght@400;600;700&display=swap" rel="stylesheet">
<style>
  :root {
    --navy: #1f2d5a;
    --orange: #f15a29;
    --peach: #fde9df;
    --lavender: #dcdce6;
    --paper: #ffffff;
    --backdrop: #e4e4e4;
  }
  * { margin: 0; padding: 0; box-sizing: border-box; }
  html, body {
    width: 1200px; height: 686px; overflow: hidden;
    background: var(--backdrop);
    font-family: "Open Sans", Arial, sans-serif;
  }
  .letterhead {
    position: absolute;
    left: 352px; top: 22px;
    width: 496px; height: 642px;
    background: var(--paper);
    box-shadow: 0 6px 18px rgba(0,0,0,0.12);
    overflow: hidden;
  }
  .masthead {
    position: absolute; left: 0; right: 0; top: 0; height: 92px;
  }
  .brand-name {
    position: absolute; left: 0; right: 0; top: 52px;
    text-align: center;
    font-size: 17px; font-weight: 700; letter-spacing: 0.5px;
    color: var(--navy);
    text-transform: uppercase;
  }
  .brand-dot {
    display: inline-block; width: 9px; height: 9px; border-radius: 50%;
    background: var(--orange); margin-right: 8px; vertical-align: 2px;
  }
  .rule {
    position: absolute; left: 0; right: 0; top: 88px;
    height: 1.5px; background: var(--navy);
  }
  .rule-accent {
    position: absolute; left: 178px; width: 140px; top: 86.5px;
    height: 4px; background: var(--orange);
  }
  .corner-emblem {
    position: absolute; left: 0; bottom: 0;
    width: 300px; height: 290px;
    background:
      radial-gradient(circle at 30% 100%, var(--peach) 0%, rgba(253,233,223,0.6) 45%, rgba(253,233,223,0) 75%),
      radial-gradient(circle at 0% 70%, var(--lavender) 0%, rgba(220,220,230,0) 60%);
  }
  .contact {
    position: absolute; left: 26px; bottom: 28px;
    list-style: none;
    font-size: 11.5px; line-height: 19px;
    color: var(--navy);
  }
  .contact li { display: flex; align-items: center; gap: 7px; }
  .contact svg { width: 11px; height: 11px; flex: none; }
  .contact .highlight { color: var(--orange); }
  .tagline {
    position: absolute; left: 26px; bottom: 10px;
    font-size: 11px; letter-spacing: 0.3px;
    color: var(--orange); text-transform: uppercase;
  }
</style>
</head>
<body>
  <main class="letterhead">
    <header class="masthead">
      <div class="brand-name"><span class="brand-dot"></span>Copper Ridge Inquiries</div>
      <div class="rule"></div>
      <div class="rule-accent"></div>
    </header>

    <div class="corner-emblem" role="img" aria-label="Faint sunburst brand decoration in peach and lavender"></div>

    <ul class="contact">
      <li>
        <svg viewBox="0 0 12 12" aria-hidden="true"><path d="M3 1 L5 3.5 L4 5 Q5 7 7 8 L8.5 7 L11 9 L9.5 11 Q4 10.5 1 3 Z" fill="var(--orange)"/></svg>
        210.555.0142
      </li>
      <li>
        <svg viewBox="0 0 12 12" aria-hidden="true"><path d="M6 11.5 C3 7.5 2 6 2 4.3 A4 4 0 0 1 10 4.3 C10 6 9 7.5 6 11.5 Z" fill="var(--orange)"/><circle cx="6" cy="4.3" r="1.5" fill="#fff"/></svg>
        Marble Falls, TX
      </li>
      <li>
        <svg viewBox="0 0 12 12" aria-hidden="true"><circle cx="6" cy="4.5" r="3.5" fill="var(--orange)"/><path d="M4 7.5 L3.5 11.5 L6 10 L8.5 11.5 L8 7.5 Z" fill="var(--orange)"/></svg>
        License NO. <span class="highlight">00427316</span>
      </li>
      <li>
        <svg viewBox="0 0 12 12" aria-hidden="true"><rect x="1" y="2.5" width="10" height="7" fill="var(--orange)"/><path d="M1 2.5 L6 6.5 L11 2.5" stroke="#fff" stroke-width="1" fill="none"/></svg>
        morgan@copperridgeinquiries.com
      </li>
    </ul>
    <p class="tagline">Over 20 years of investigative experience</p>
  </main>
</body>
</html>
```